Logo and bag for Turkish coffee brand

We are a coffee roasting company. We need a logo for our new Turkish coffee brand. We are targeting C+ to A- customer segment. Our brand is above average in pricing and can be expressed as very good in quality or a bit less than excellentOur brand name is قهواكQahwakIt is an Arabic word that means "Your coffee" and if read in a different way it means "I love You"

Target Market(s)

We are selling in Egyptian market for customer segments from C+ and up to A-

Logo Text

Bunnyar بنّيار

Requirements
Must have
• 1. The logo must contain brand name in Arabic good to have it in Arabic and English if possible.
• 2. All text content must be in Arabic and good to be in both Arabic and English
• 3. The package must include two spaces for limited text paragraphs
• an area for production date and expiry.
• 4. An area for selecting variants of the product. Our coffee has light-medium-dark roasted (فاتح - وسط - غامق)
• Plain or flavored (سادة - محوج)

```html
<!DOCTYPE html>
<html lang="en">
<head>
<meta charset="utf-8">
<title>Bunnyar Turkish Coffee Bag</title>
<link href="https://fonts.googleapis.com/css2?family=Josefin+Sans:wght@300;400&family=Reem+Kufi:wght@500;700&family=Gochi+Hand&display=swap" rel="stylesheet">
<style>
  :root {
    --backdrop: #e9e2d4;
    --bag-dark: #3e3128;
    --bag-mid: #5a4a3f;
    --bag-light: #6d5c50;
    --seal: #4a3d35;
    --gold: #c8a874;
    --gold-soft: #b8976a;
    --cream: #f4efe6;
    --steel: #9a8e80;
  }
  * { margin: 0; padding: 0; box-sizing: border-box; }
  html, body { width: 1200px; height: 789px; overflow: hidden; }
  body {
    background: var(--backdrop);
    display: flex;
    justify-content: center;
    align-items: center;
  }
  .bag {
    position: relative;
    width: 390px;
    height: 740px;
    background: linear-gradient(160deg, var(--bag-light) 0%, var(--bag-mid) 45%, var(--bag-dark) 100%);
    border-radius: 4px;
    box-shadow: 0 14px 30px rgba(60, 45, 30, 0.28);
    display: flex;
    flex-direction: column;
    align-items: center;
    overflow: hidden;
  }
  .bag__seal {
    width: 100%;
    height: 26px;
    background: var(--seal);
    border-bottom: 1px solid rgba(0,0,0,0.25);
  }
  .bag__pattern-band {
    width: 100%;
    height: 96px;
    background: linear-gradient(180deg, #3b2f27 0%, #4a3b31 100%);
    border-bottom: 1px solid rgba(200,168,116,0.35);
  }
  .brand {
    margin-top: 26px;
    text-align: center;
    color: var(--gold);
  }
  .brand__latin {
    font-family: "Josefin Sans", sans-serif;
    font-weight: 300;
    font-size: 44px;
    letter-spacing: 3px;
    line-height: 1;
  }
  .brand__arabic {
    font-family: "Reem Kufi", sans-serif;
    font-weight: 700;
    font-size: 58px;
    line-height: 1.2;
    margin-top: 4px;
  }
  .tagline {
    font-family: "Gochi Hand", cursive;
    font-size: 28px;
    color: var(--cream);
    margin-top: 6px;
    letter-spacing: 1px;
  }
  .serving-visual {
    margin-top: 30px;
    width: 300px;
    height: 210px;
    border-radius: 50% / 38%;
    background: radial-gradient(ellipse at 55% 45%, #b7ab9b 0%, var(--steel) 35%, #6b5d50 75%, transparent 100%);
  }
  .variant {
    margin-top: 34px;
    text-align: center;
    color: var(--cream);
  }
  .variant__arabic {
    font-family: "Reem Kufi", sans-serif;
    font-weight: 700;
    font-size: 34px;
    line-height: 1.1;
  }
  .variant__latin {
    font-family: "Josefin Sans", sans-serif;
    font-weight: 400;
    font-size: 17px;
    margin-top: 6px;
  }
  .variant__weight {
    font-family: "Josefin Sans", sans-serif;
    font-weight: 400;
    font-size: 16px;
    margin-top: 8px;
  }
</style>
</head>
<body>
  <main class="bag">
    <div class="bag__seal"></div>
    <div class="bag__pattern-band" role="img" aria-label="Gold geometric star pattern band on dark brown"></div>
    <header class="brand">
      <div class="brand__latin">BUNNYAR</div>
      <div class="brand__arabic" lang="ar" dir="rtl">بنّيار</div>
    </header>
    <p class="tagline">Turkish Coffee Brand</p>
    <div class="serving-visual" role="img" aria-label="Photo of a steaming copper cezve and a cup of Turkish coffee on an engraved metal tray"></div>
    <section class="variant">
      <div class="variant__arabic" lang="ar" dir="rtl">غامق</div>
      <div class="variant__latin">DARK ROASTED</div>
      <div class="variant__weight">500g</div>
    </section>
  </main>
</body>
</html>
```